Banner for Vet Hospital 5m x 1.2m - Heat Stroke

Meadowlark Pet Hospital needs a Heat Stroke Banner for Summer.
The banner will be 5000mm long and 1200mm tall.

Our region has been hot this year and this summer is going to be extremely hot.
I want to warn people about heat stroke.
I want you to create a heat stroke banner that conveys the symptoms of heat stroke.

Pictures are better than words.
There should be IMAGES and WORDS that can be seen from the road 30m away and maybe some smaller words for people to read as they walk past.

Here are some of the signs of Heat Stroke:
- Panting which increases as heatstroke progresses
- Drooling, salivating
- Agitation, restlessness
- Very red or pale gums
- Bright red tongue
- Increased heart rate
- Breathing distress
- Vomiting Diarrhea (possibly with blood)
- Signs of mental confusion, delirium
- Dizziness, staggering
- Lethargy, weakness
- Muscle tremors
- Seizures
- Collapsing and lying down
- Little to no urine production
- Coma

I have attached characters that we often use in our advertising. They are optional.
I have done a mock up of the design I imagine. You could refine this design or make your own....or both.

Target Market(s)

Women aged 20 to 50.

Industry/Entity Type

Veterinary

Font styles to use
Sans Serif

Colors
fbed22
f78f20
ec1f27
ffffff

Requirements
Must have
• Heat Stroke Symtpms.
• Heat Stroke Warning.
• Summer theme.
Nice to have
• Bright colours.

```html
<!DOCTYPE html>
<html lang="en">
<head>
<meta charset="utf-8">
<title>Heat Stroke Summer Banner</title>
<link rel="stylesheet" href="https://fonts.googleapis.com/css2?family=Oswald:wght@400;500;600;700&family=Open+Sans:wght@700;800&display=swap">
<style>
  :root {
    --sun-yellow: #fbed22;
    --cream: #fbf1c4;
    --cream-light: #fdf7dc;
    --orange: #f78f20;
    --orange-deep: #f26a21;
    --red: #ec1f27;
    --white: #ffffff;
    --green: #8cc63f;
    --list-orange: #f47b20;
    --fur-dark: #5b4330;
    --fur-light: #b98a5c;
  }
  * { margin: 0; padding: 0; box-sizing: border-box; }
  html, body {
    width: 1200px; height: 1200px; overflow: hidden;
    background: var(--white);
  }
  .banner {
    position: absolute; left: 30px; top: 463px;
    width: 1140px; height: 274px; overflow: hidden;
    background: radial-gradient(ellipse at 92% 60%, var(--cream-light) 0%, var(--cream) 55%, #f8eab0 100%);
  }
  .banner-shapes { position: absolute; inset: 0; width: 100%; height: 100%; }
  .dog-photo {
    position: absolute; left: 40px; top: 30px; width: 255px; height: 244px;
    border-radius: 120px 120px 0 0;
    background: linear-gradient(160deg, var(--fur-light) 0%, #8a6442 45%, var(--fur-dark) 100%);
    border: 5px solid var(--white); border-bottom: none;
  }
  .tagline {
    position: absolute; left: 283px; top: 21px; width: 302px; height: 23px;
    background: var(--green);
    clip-path: polygon(0 0, 100% 0, 97% 50%, 100% 100%, 0 100%, 3% 50%);
    color: var(--white);
    font: 600 17px/23px "Oswald", sans-serif; text-align: center; letter-spacing: -0.3px;
  }
  .headline {
    position: absolute; left: 281px; top: 42px;
    font-family: "Oswald", sans-serif; font-weight: 700;
    font-size: 74px; line-height: 64.5px; letter-spacing: -1.5px;
    text-transform: uppercase;
  }
  .headline span { display: block; }
  .headline .line-1 { color: var(--orange-deep); }
  .headline .line-2 { color: #ef4f23; }
  .headline .line-3 { color: var(--red); }
  .symptoms-title {
    position: absolute; left: 707px; top: 32px;
    font: 800 15.5px/20px "Open Sans", sans-serif; color: var(--list-orange);
    letter-spacing: -0.2px;
  }
  .symptoms {
    position: absolute; top: 64px; list-style: none;
    font: 400 10.2px/17.6px "Oswald", sans-serif; color: var(--list-orange);
    text-transform: uppercase;
  }
  .symptoms.col-1 { left: 707px; }
  .symptoms.col-2 { left: 929px; }
  .symptoms li { position: relative; padding-left: 15px; }
  .symptoms li.cont::before { display: none; }
  .symptoms li::before {
    content: "✓"; position: absolute; left: 0; top: 4px;
    width: 10px; height: 10px; border-radius: 50%;
    background: var(--green); color: var(--white);
    font: 700 7px/10px "Open Sans", sans-serif; text-align: center;
  }
</style>
</head>
<body>
  <section class="banner" aria-label="Heat stroke summer banner">
    <svg class="banner-shapes" viewBox="0 0 1140 274" preserveAspectRatio="none" aria-hidden="true">
      <polygon points="0,0 1140,0 1140,3 0,22" fill="var(--orange)"/>
      <polygon points="0,274 1140,274 1140,222 1080,225 0,262" fill="var(--orange)"/>
      <polygon points="0,274 1140,274 1140,248 0,268" fill="var(--orange-deep)"/>
      <g fill="var(--white)">
        <circle cx="1105" cy="265" r="30"/>
        <circle cx="1135" cy="245" r="26"/>
        <circle cx="1070" cy="272" r="20"/>
        <circle cx="10" cy="150" r="24"/>
        <circle cx="30" cy="170" r="20"/>
      </g>
    </svg>

    <div class="dog-photo" role="img" aria-label="Photo of a panting dog with tongue out and leather collar"></div>

    <div class="tagline">DO NOT LET YOUR DOGS OVERHEATED</div>

    <h1 class="headline">
      <span class="line-1">Get your pet</span>
      <span class="line-2">hydrate this</span>
      <span class="line-3">summer</span>
    </h1>

    <h2 class="symptoms-title">HERE ARE SOME OF THE SIGNS OF HEAT STROKE</h2>
    <ul class="symptoms col-1">
      <li>Panting which increases as</li>
      <li class="cont">heatstroke progresses</li>
      <li>Drooling, salivating</li>
      <li>Agitation, restlessness</li>
      <li>Very red or pale gums</li>
      <li>Bright red tongue</li>
      <li>Increased heart rate</li>
      <li>Breathing distress</li>
      <li>Vomiting diarrhea (possibly with blood)</li>
    </ul>
    <ul class="symptoms col-2">
      <li>Dizziness, staggering</li>
      <li>Lethargy, weakness</li>
      <li>Muscle tremors</li>
      <li>Seizures</li>
      <li>Collapsing and lying down</li>
      <li>Little to no urine production</li>
      <li>Coma</li>
      <li>Signs of mental confusion, delirium</li>
    </ul>
  </section>
</body>
</html>
```